Vardo Kinship UAE - Website for Club Members

Vardo Kinship UAE Website

A simple but amazing website is needed for an offroad club in the UAE.

Vardokinship.ae (domain owned)
Hosting required.

Vardo Kinship UAE is a non-profit club that brings together Vardo owners who meet up and drive & gather together all over the country.

The club until now has been working on WhatsApp but has grown to over 700+ members and needs a website to support it and have a platform to book/sign up for trips. As there are many types of driving levels, we need a platform to categorise each member according to their driving skill so they can only signup for the trip that is in accordance with their level.

The page must be intuitive, easy and clean. We have many members from many different countries & ages. Keeping it simple would be good.
English is the main language. (Maybe an easy Google translation addon for Arabic)

Mobile friendly / web app:
Most of our members will use the page on their mobile, and admins will usually use the site on their mobiles to see who is on the trip, show reports, blog etc.

1. Member profile creation
● Login
● Sign up
● Recover password
• (Terms & Conditions Button) Captcha

2. Member Area
● Dynamic ranking (Admins to set levels)
• Master Admin (Master Access)
• Admins (Full Access)
• Management (Edit Options)
• Marshalls (Can Post Trips & add post-trip report)

● Member Level
• Brisk (Beginner)
• Tavola (Intermediate)
• Morvane (Advanced)
• Halberd (Expert)
• 518 (Teacher)
● Profile (Vehicle & Member info)

3. Member trip/events sign-ups
• Members can only see trips according to their tier
• (Example) Only Brisk Should see Trips for “Brisk Level” / Tavola can see Tavola Trips & Brisk Trips / Morvane can see Morvane, Tavola & Brisk Trips etc. Tiers can only see their level and below.
● A page with the list of trips (group by date)
● Sign up/out button
● The trip will contain:
○ Title
○ Picture
○ Description
○ Time and Location
○ Level limit
○ Trip creator/owner
○ Trip capacity limit
● Admin: add/remove members from trip
● Admin can create/manage trips
● Admin can rate (1 rating 1 to 5 stars) members in the trip

4. Sponsors Pages/s (tolev4x4, kev)
• Ability to add full pages according to the sponsorship level.
• Speciality Index (Fabrication, Mechanic, Wheel, Rims, painting)
● Ad area with Title, image, a short description and link

5. Vardo Kinship profile
• About Us page
• Rules and regulations, T&C’s.
• Roles
• Founders/Management area.

6, Blog Area.
• General blog, nothing complicated
• For example, an area where members can sell their used items, an area where they can chit-chat about new models etc.
• Only Admins can create posts/subjects.
• Blogs post should also be seen as per Member Level

7, Social media area.
● Simple place where we share our social media. @vardokinship.ae
• We only use Instagram for now but we will push Tik Tok soon.

8, E-Commerce
• Not a must at this moment but will be required in the future (1 year). Please account for this so we can activate it when required. Simple and easy.

9, Backend

• Backend Should be straightforward to use and intuitive, adding images/text, editing images/text, creating text (Font, size, colour), and adding pages. (For simple people to use one site). We do not require website management, but we will contact the developer if we need any big add-ons or want to expand the site.
• Mobile view is essential.
o We will use the website as a Web App for mobile devices. Mobile versions should be accessible, mobile like and intuitive.
• Apple Wallet / Google Wallet Membership Card option required. Members will be able to download their membership cards. (Simple, no picture) members details

Website References:
Vardokinship.ae (old website)
QM4x4
Pelgan 4x4
UAE Trailhands
Wistful 4x4

Target Market(s)

Club members & future club members

Industry/Entity Type

Offroad club

Coding

Coded - Design and coding required

Number of Pages Required

5+ page

Other font styles liked:
• Helvetica

Colors
0054AA
0677BA
7BADD7
CADEEF
E8F1F8
EB3D1F
EC4F4E
F09395
F8D3D4
FCEDEE

Requirements
Must have
• Member/Profile Area, Member Level, Trips/Events area, Sponsors, Profile, Blog, E-commerce, easy & intuative backend.
Nice to have
• Simple, clean, attaractive, modern. Apple Wallet & Google Wallet option for memebers to downalod their mebership cards.
Should not have
• A very complicated backend.

```html
<!DOCTYPE html>
<html lang="en">
<head>
<meta charset="utf-8">
<title>Vardo Kinship UAE</title>
<link href="https://fonts.googleapis.com/css2?family=Montserrat:wght@300;400;600&family=Open+Sans:wght@400;700;800&display=swap" rel="stylesheet">
<style>
:root{
  --ink:#111;
  --headline:#0e3f4f;
  --dark:#3b3b3b;
  --grey:#8a8a8a;
  --blog-bg:#ebe9ea;
  --line:#a9a9a9;
  --card-border:#d9b6d2;
  --partner:#1d5aa0;
  --nav-arrow:#3d4a6b;
}
*{margin:0;padding:0;box-sizing:border-box}
html,body{width:1200px;height:3373px;overflow:hidden;background:#fff}
body{position:relative;font-family:"Montserrat",Helvetica,Arial,sans-serif;color:var(--ink)}
.abs{position:absolute}
.photo{position:absolute}
.section-line{position:absolute;left:0;width:1200px;height:2px;background:var(--line)}

/* hero */
.hero-photo{left:0;top:0;width:620px;height:677px;
  background:
    radial-gradient(ellipse 55% 30% at 78% 52%,rgba(255,214,222,.95) 0%,rgba(232,160,190,.6) 40%,rgba(232,160,190,0) 100%),
    linear-gradient(180deg,#5e4670 0%,#8f6a98 22%,#c48fb2 45%,#9a6f93 60%,#6a4d6f 78%,#3c2c42 100%)}
.brand-tag{left:0;top:18px;background:#fff;padding:2px 14px 4px 16px;font-size:45px;font-weight:400;line-height:1.2}
.menu-btn{left:1135px;top:0;width:65px;height:63px;background:var(--dark)}
.headline{left:668px;top:88px;width:530px;font-family:"Open Sans",sans-serif;font-weight:800;font-size:60px;line-height:71px;color:var(--headline);white-space:nowrap}
.hero-sub{left:677px;top:446px;width:470px;font-family:"Open Sans",sans-serif;font-size:21px;line-height:26px;color:#333}
.signup-btn{left:677px;top:546px;width:459px;height:62px;background:var(--dark);color:#fff;font-family:"Open Sans",sans-serif;font-weight:700;font-size:37px;text-align:center;line-height:60px}
.hero-links{left:788px;top:616px;font-family:"Open Sans",sans-serif;font-size:17px;color:var(--grey)}
.hero-links a{color:var(--grey);text-decoration:underline;margin-right:28px}

/* story */
.story-photo{left:0;top:677px;width:620px;height:673px;
  background:
    linear-gradient(115deg,rgba(70,50,80,.55) 0%,rgba(70,50,80,0) 40%,rgba(70,50,80,.45) 70%,rgba(70,50,80,0) 100%),
    linear-gradient(180deg,#8b7596 0%,#a896b1 35%,#7a6485 65%,#9c8aa6 100%)}
.play-icon{left:270px;top:974px;width:100px;height:100px}
.section-title{font-size:44px;font-weight:400;text-align:center}
.story-title{left:656px;top:712px;width:520px}
.story-text{left:656px;top:800px;width:522px;font-size:17.4px;line-height:29.4px}
.story-link{left:653px;top:1282px;font-size:23px;color:var(--grey);text-decoration:underline}

/* blogs */
.blog-bg{left:620px;top:1350px;width:580px;height:674px;background:var(--blog-bg)}
.blog-photo{left:0;top:1350px;width:620px;height:674px;
  background:linear-gradient(180deg,#b58664 0%,#c9a58a 9%,#a9bbcb 18%,#5c7fb8 26%,#1c50c4 36%,#0b43b8 60%,#0a3598 82%,#06246c 100%)}
.blog-title{left:700px;top:1390px;width:410px}
.blog-card{left:320px;top:1512px;width:559px;height:344px;background:#fff;border:2px solid var(--card-border)}
.blog-date{left:38px;top:30px;font-size:25px;color:var(--grey)}
.blog-head{left:38px;top:126px;width:500px;font-size:29px;line-height:36px;color:#333;font-weight:400}
.read-more{left:38px;top:282px;font-size:21px;font-weight:600;color:var(--grey);display:flex;align-items:center;gap:14px}
.round-arrow{width:72px;height:72px;border-radius:50%;background:#fff}

/* gallery */
.gallery-title{left:0;top:2082px;width:1200px}
.gallery-photo{top:2230px;width:272px;height:364px;border:1px dashed #999}
.g1{left:120px;background:linear-gradient(180deg,#d8d2dc 0%,#8a6a5e 22%,#c9a99a 45%,#7a5a4c 65%,#ebe6ea 85%,#d6cfd8 100%)}
.g2{left:461px;background:linear-gradient(180deg,#1f5ecf 0%,#2f72de 42%,#4a4f66 62%,#c99868 74%,#b88a5c 100%)}
.g3{left:802px;background:linear-gradient(180deg,#aeb9c9 0%,#c9ced6 18%,#4c5260 40%,#3a3e49 62%,#8f8a86 80%,#b3aea8 100%)}

/* footer */
.footer-brand{left:20px;top:2732px;font-family:"Open Sans",sans-serif;font-weight:700;font-size:44px}
.footer-copy{left:32px;top:2790px;font-size:25px;color:#333}
.footer-col{top:2862px;font-size:25px;line-height:31px;color:#333}
.footer-col h3{font-weight:400;font-size:26px;color:var(--ink);margin-bottom:30px}
.legal{left:24px;top:3208px;font-size:21px;color:#333}
.legal a{color:#333;text-decoration:underline;margin-right:24px}
.footer-mark{left:20px;top:3268px;font-family:"Open Sans",sans-serif;font-weight:800;font-size:58px;color:var(--ink);line-height:1.2}
.partner{left:200px;top:3298px;font-size:21px;color:var(--partner)}
.footer-photo{left:630px;top:2748px;width:570px;height:590px;border-radius:60px 40px 90px 90px;
  background:linear-gradient(180deg,#4a4d5c 0%,#3a3d4b 30%,#575a6c 55%,#2e303b 78%,#cfcad8 100%)}
</style>
</head>
<body>

<!-- hero -->
<div class="photo hero-photo" role="img" aria-label="Off-road vehicle parked on a gravel track at sunset, purple tint"></div>
<div class="abs brand-tag">Vardo Kinship.</div>
<div class="abs menu-btn">
  <svg width="65" height="63" viewBox="0 0 65 63"><g fill="#fff"><rect x="20" y="19" width="26" height="4"/><rect x="20" y="29" width="26" height="4"/><rect x="20" y="39" width="26" height="4"/></g></svg>
</div>
<h1 class="abs headline">“Unleash<br>Your Inner<br>Adventurer with<br>Vardo Kinship<br>Offroad Club”?</h1>
<p class="abs hero-sub">Take your passion for offroading to the next level and join a community of like-minded adventurers.</p>
<div class="abs signup-btn">Sign Up</div>
<div class="abs hero-links"><a>Sign In</a><a>Terms and Condition</a></div>
<div class="section-line" style="top:676px"></div>

<!-- story -->
<div class="photo story-photo" role="img" aria-label="Aerial view of rugged mountain ridges, purple tint"></div>
<svg class="abs play-icon" viewBox="0 0 100 100" aria-label="Play video">
  <circle cx="50" cy="50" r="46" fill="#fff" fill-opacity=".9"/>
  <path d="M40 32v36l30-18z" fill="#3b3b3b"/>
</svg>
<h2 class="abs section-title story-title">Our Story</h2>
<p class="abs story-text">Welcome to Vardo Kinship Offroad Club, where adventure meets offroading. Our club is dedicated to providing members with the ultimate offroading experience, exploring some of the most scenic and challenging trails in the country. Our community is made up of passionate offroad enthusiasts who share a love for exploration, adrenaline, and the great outdoors. Our fleet of 4x4 Vardos is equipped with the latest technology and features, ensuring a safe and comfortable ride even on the toughest terrain. With features like electronic locking differentials, sway bar disconnect, and hill descent control, our Vardos can handle any obstacle in their path. Whether you're an experienced offroader or a newbie, our club has something to offer. Join us today and experience the ultimate combination of cutting-edge technology and breathtaking offroading adventures.</p>
<a class="abs story-link">&lt;&lt;View More Videos</a>
<div class="section-line" style="top:1349px"></div>

<!-- blogs -->
<div class="abs blog-bg"></div>
<div class="photo blog-photo" role="img" aria-label="Blue off-road vehicle bonnet against desert hills"></div>
<h2 class="abs section-title blog-title">Our Blogs</h2>
<div class="abs round-arrow" style="left:122px;top:1669px">
  <svg width="72" height="72" viewBox="0 0 72 72"><path d="M46 36H26M33 29l-7 7 7 7" fill="none" stroke="#222" stroke-width="2.5" stroke-linecap="round" stroke-linejoin="round"/></svg>
</div>
<div class="abs round-arrow" style="left:1019px;top:1669px">
  <svg width="72" height="72" viewBox="0 0 72 72"><path d="M26 36h20M39 29l7 7-7 7" fill="none" stroke="#222" stroke-width="2.5" stroke-linecap="round" stroke-linejoin="round"/></svg>
</div>
<article class="abs blog-card">
  <div class="abs blog-date">November 17,2018</div>
  <h3 class="abs blog-head">518: The Quickest, Most Powerful Tramont Ever</h3>
  <div class="abs read-more">Read Article
    <svg width="44" height="20" viewBox="0 0 44 20"><path d="M1 10h40M33 3l8 7-8 7" fill="none" stroke="#333" stroke-width="2.5" stroke-linecap="round" stroke-linejoin="round"/></svg>
  </div>
</article>
<div class="section-line" style="top:2023px"></div>

<!-- gallery -->
<h2 class="abs section-title gallery-title">Our Gallery</h2>
<svg class="abs" style="left:30px;top:2396px" width="30" height="34" viewBox="0 0 30 34"><path d="M22 3L8 17l14 14" fill="none" stroke="var(--nav-arrow)" stroke-width="7"/></svg>
<div class="photo gallery-photo g1" role="img" aria-label="Portrait of a smiling club member"></div>
<div class="photo gallery-photo g2" role="img" aria-label="Member standing beside an off-road vehicle on desert dunes"></div>
<div class="photo gallery-photo g3" role="img" aria-label="Member posing next to a dark off-road vehicle"></div>
<svg class="abs" style="left:1120px;top:2396px" width="30" height="34" viewBox="0 0 30 34"><path d="M8 3l14 14L8 31" fill="none" stroke="var(--nav-arrow)" stroke-width="7"/></svg>
<div class="section-line" style="top:2699px"></div>

<!-- footer -->
<div class="photo footer-photo" role="img" aria-label="Dark grey lifted off-road vehicle with roof light bar"></div>
<div class="abs footer-brand">Vardo Kinship.</div>
<div class="abs footer-copy">© 2021 Dubai, UAE</div>
<nav class="abs footer-col" style="left:16px"><h3>The Club</h3>About<br>Contact</nav>
<nav class="abs footer-col" style="left:204px"><h3>Forum</h3>Your Posts<br>Board Index<br>New Posts<br>Unread Posts<br>Unanswered<br>Active Topics</nav>
<nav class="abs footer-col" style="left:436px"><h3>Events</h3>All Trips<br>Trips by levels<br>Trips Archive<br>Calendar View<br>Create Trip<br>Edit Trips<br>Manage<br>Registrants</nav>
<div class="abs legal"><a>Privacy Policy</a><a>Disclaimer</a></div>
<div class="abs footer-mark">Vardo</div>
<div class="abs partner">Coastal Motors LLC</div>

</body>
</html>
```